GPS Tracker Business Card Design

We need a business card for a GPS Vehicle tracking company. We sell the hardware for the vehicle and the software platform to monitor your vehicle/s. Including high asset non-powered vehicles like a trailer using our solar powered unit.
We like using dark blue to different shades of blue along with gold. We have phone apps for Android and Apple devices.

We have a platform for families wanting to track their teenage driver and children; Plus a Fleet vehicle tracking platform.

Features: unlimited number of vehicles and/or assets including snow mobiles forklifts generators trailers airport equipment

Reports for driving behavior reports and alerts dashboard fleet maintenace timeline view and replay geofence real time alerts logbook scheduling route optimization accounting integration fleet grouping closest vehicle locator On Board Diagnostics.

Benefits: Increased productivity improved fuel efficiency organizing your business improve time management simplify back end processes, reduce fleet fuel efficiency and expenses increase fleet security etc..

Please view website: Velmorix.com

Industry/Entity Type

Business

Contact Information for Business Card

Harold P Simkins

```html
<!DOCTYPE html>
<html lang="en">
<head>
<meta charset="utf-8">
<title>Velmorix Business Card</title>
<link rel="stylesheet" href="https://fonts.googleapis.com/css2?family=Open+Sans:wght@400;600;700&display=swap">
<style>
  :root {
    --page-bg: #e4e6e8;
    --card-bg: #f4f5f6;
    --card-edge: #b9bdc2;
    --ink: #3d3f42;
    --ink-soft: #55585c;
    --brand-blue: #0b3a8c;
    --rule: #6d7075;
    --map-tone: #e2e5e8;
  }
  * { box-sizing: border-box; margin: 0; padding: 0; }
  html, body {
    width: 1200px; height: 970px; overflow: hidden;
    background: var(--page-bg);
    font-family: "Open Sans", Arial, sans-serif;
  }
  .card {
    position: absolute; left: 170px; top: 245px;
    width: 860px; height: 480px;
    background: var(--card-bg);
    border: 1.5px solid var(--card-edge);
    border-radius: 22px;
    box-shadow: 0 10px 30px rgba(0,0,0,0.12);
    overflow: hidden;
  }
  .world-map {
    position: absolute; left: 320px; top: 40px; width: 510px; height: 390px;
    background: radial-gradient(ellipse at 50% 45%, var(--map-tone) 0%, rgba(226,229,232,0.5) 55%, rgba(244,245,246,0) 75%);
  }
  .brand-name {
    position: absolute; left: 42px; top: 62px;
    font-size: 58px; font-weight: 400; color: var(--ink);
    letter-spacing: -1px; line-height: 1;
  }
  .rule {
    position: absolute; left: 42px; top: 302px; width: 572px; height: 1.5px;
    background: var(--rule);
  }
  .person {
    position: absolute; right: 40px; top: 258px; text-align: right;
  }
  .person-name {
    font-size: 27px; font-weight: 700; color: var(--brand-blue); line-height: 1.2;
  }
  .person-title {
    font-size: 19px; color: var(--ink-soft); line-height: 1.4;
  }
  .contacts {
    position: absolute; left: 42px; top: 328px; list-style: none;
  }
  .contacts li {
    display: flex; align-items: center; gap: 8px;
    font-size: 19px; color: var(--ink-soft); height: 28px;
  }
  .contacts svg { width: 17px; height: 17px; fill: var(--ink); flex: none; }
  .address {
    position: absolute; right: 40px; top: 372px; text-align: right;
    font-size: 19px; color: var(--ink-soft); line-height: 28px;
  }
</style>
</head>
<body>
  <div class="card">
    <div class="world-map" role="img" aria-label="Faint world map in the card background"></div>

    <div class="brand-name">Velmorix</div>

    <div class="person">
      <div class="person-name">Harold P Simkins</div>
      <div class="person-title">Managing Parthner</div>
    </div>

    <div class="rule"></div>

    <ul class="contacts">
      <li>
        <svg viewBox="0 0 16 16" aria-hidden="true"><path d="M1 5c0-2 3-3 7-3s7 1 7 3v1.5h-4V5H5v1.5H1z M3 8l2-2h6l2 2v6H3z"/></svg>
        + 000 000 0000
      </li>
      <li>
        <svg viewBox="0 0 16 16" aria-hidden="true"><path d="M4 1h8v4H4z M1 6h14v6h-3v-2H4v2H1z M5 11h6v4H5z"/></svg>
        + 000 000 0000
      </li>
      <li>
        <svg viewBox="0 0 16 16" aria-hidden="true"><path d="M1 3h14v10H1z" fill="none" stroke="#3d3f42" stroke-width="1.6"/><path d="M1 3l7 6 7-6" fill="none" stroke="#3d3f42" stroke-width="1.6"/></svg>
        info@Velmorix.com
      </li>
      <li>
        <svg viewBox="0 0 16 16" aria-hidden="true"><circle cx="8" cy="8" r="6.5" fill="none" stroke="#3d3f42" stroke-width="1.6"/><path d="M1.5 8h13 M8 1.5c-3 3-3 10 0 13 M8 1.5c3 3 3 10 0 13" fill="none" stroke="#3d3f42" stroke-width="1.2"/></svg>
        www.Velmorix.com
      </li>
    </ul>

    <div class="address">
      215 Corrimal Ridge Rd<br>
      Tallowvale, QLD, 4275
    </div>
  </div>
</body>
</html>
```